Business Card Design Project

Use newly designed logo and tie into newly designed website
I need a new logo and website layout designed for my partner's business. This is a birthday present. His business is interior painting, wallpapering and design. He also has access to a wide variety of products including carpet, fabrics, furniture, wallpaper, tile, countertops, etc. I have attached some screen shots of his website for reference. He is a one man shop and has a stellar reputation with his customers. He is on-time, very tidy, excellent with animals, and always finishes on time and on budget. There are no restrictions on colors or fonts. The logo needs to work well with the website, business cards and printed materials. The website needs to flow content for device size so it looks just as good on a cell phone or tablet as it does on a desktop computer. Whatever the heck that's called!Thanks. I am looking forward to seeing everyone's ideas.
Updates
Hi Designers,
We've reopened this project as our logo design project has just completed.
Please refer to the uploaded files and make use of either Horizontal or Vertical versions of the logo depending on what you think is suitable for your design proposals.
We look forward to your creative submissions!
Target Market(s)
Consumers looking to improve the interior environment of their homes by updating wall paint or paper, flooring (either carpet, tile, or hardwoods), counter tops, window treatments, etc. Clients tend to be more upper middle class and have certain taste levels and expectations. New logo, website and business card should align to meet those levels.
Industry/Entity Type
Cell Phone
Look and feel
Each slider illustrates characteristics of the customer's brand and the style your logo design should communicate.

```html
<!DOCTYPE html>
<html lang="en">
<head>
<meta charset="utf-8">
<title>Quorvell Interior Designs – Business Card</title>
<link rel="stylesheet" href="https://fonts.googleapis.com/css2?family=Montserrat:wght@400;600;700&display=swap">
<style>
  :root {
    --backdrop: #ecebe6;
    --card-front: #ffffff;
    --card-back: #f6f4c4;
    --card-back-edge: #e6e2ad;
    --navy: #221c4a;
    --maroon: #7a1712;
    --orange: #f2931c;
    --ink: #1e1e1e;
    --rule: #a99a72;
    --shadow: rgba(0, 0, 0, 0.18);
  }
  * { box-sizing: border-box; margin: 0; padding: 0; }
  html, body {
    width: 1200px;
    height: 1000px;
    overflow: hidden;
  }
  body {
    background: var(--backdrop);
    font-family: "Montserrat", Arial, sans-serif;
    position: relative;
  }
  .card {
    position: absolute;
    left: 220px;
    width: 760px;
    height: 430px;
    border-radius: 34px;
    box-shadow: 0 8px 22px var(--shadow);
  }

  /* Front card */
  .card--front {
    top: 45px;
    background: var(--card-front);
  }
  .brand-block {
    position: absolute;
    left: 60px;
    top: 130px;
    width: 300px;
    text-align: center;
  }
  .brand-block__square {
    width: 100px;
    height: 100px;
    margin: 0 auto 14px;
    background: var(--navy);
  }
  .brand-block__name {
    color: var(--navy);
    font-weight: 700;
    font-size: 20px;
    line-height: 1.2;
    letter-spacing: 0.5px;
    text-transform: uppercase;
    white-space: nowrap;
  }
  .holder {
    position: absolute;
    left: 420px;
    top: 130px;
  }
  .holder__name {
    color: var(--maroon);
    font-weight: 700;
    font-size: 28px;
    line-height: 1.2;
  }
  .holder__role {
    color: var(--orange);
    font-weight: 600;
    font-size: 17px;
    margin-top: 2px;
  }
  .contact-list {
    position: absolute;
    left: 440px;
    top: 255px;
    list-style: none;
  }
  .contact-list__item {
    display: flex;
    align-items: center;
    gap: 12px;
    font-size: 20px;
    color: var(--ink);
    height: 30px;
    white-space: nowrap;
  }
  .contact-list__icon {
    width: 20px;
    height: 20px;
    flex: none;
    fill: var(--orange);
  }

  /* Back card */
  .card--back {
    top: 525px;
    background: var(--card-back);
    box-shadow: 4px 5px 0 var(--card-back-edge), 0 10px 24px var(--shadow);
  }
  .lockup {
    position: absolute;
    left: 100px;
    right: 100px;
    top: 110px;
  }
  .lockup__rule {
    height: 7px;
    margin: 0 12px;
    border-top: 2px solid var(--rule);
    border-bottom: 2px solid var(--rule);
  }
  .lockup__body {
    display: flex;
    align-items: center;
    justify-content: center;
    gap: 22px;
    padding: 22px 0 20px;
  }
  .lockup__square {
    width: 110px;
    height: 110px;
    flex: none;
    background: var(--navy);
  }
  .lockup__name {
    color: var(--navy);
    font-weight: 700;
    font-size: 36px;
    line-height: 1.15;
    letter-spacing: 1px;
    text-transform: uppercase;
    white-space: nowrap;
  }
</style>
</head>
<body>

<section class="card card--front">
  <div class="brand-block">
    <div class="brand-block__square"></div>
    <p class="brand-block__name">Quorvell<br>Interior Designs</p>
  </div>

  <div class="holder">
    <h1 class="holder__name">Name Here</h1>
    <p class="holder__role">Interior Designer</p>
  </div>

  <ul class="contact-list">
    <li class="contact-list__item">
      <svg class="contact-list__icon" viewBox="0 0 20 20" aria-hidden="true"><path d="M2 6c0-2 2-3 8-3s8 1 8 3v2h-4V6.5c-1-.5-7-.5-8 0V8H2z"/><path d="M5 10l2-3h6l2 3v6H5z"/><circle cx="10" cy="12" r="1.8" fill="#fff"/></svg>
      <span>(000)000-0000</span>
    </li>
    <li class="contact-list__item">
      <svg class="contact-list__icon" viewBox="0 0 20 20" aria-hidden="true"><path d="M1 4h18v12H1z"/><path d="M1 4l9 7 9-7" fill="none" stroke="#fff" stroke-width="1.6"/></svg>
      <span>email@mailbox.com</span>
    </li>
    <li class="contact-list__item">
      <svg class="contact-list__icon" viewBox="0 0 20 20" aria-hidden="true"><g fill="none" stroke="#f2931c" stroke-width="1.6"><circle cx="10" cy="10" r="8"/><ellipse cx="10" cy="10" rx="3.5" ry="8"/><path d="M2 10h16M3.5 6h13M3.5 14h13"/></g></svg>
      <span>www.quorvelldesigns.com</span>
    </li>
    <li class="contact-list__item">
      <svg class="contact-list__icon" viewBox="0 0 20 20" aria-hidden="true"><path d="M10 1a6 6 0 0 1 6 6c0 4.5-6 12-6 12S4 11.5 4 7a6 6 0 0 1 6-6z"/><circle cx="10" cy="7" r="2.2" fill="#fff"/></svg>
      <span>address type here</span>
    </li>
  </ul>
</section>

<section class="card card--back">
  <div class="lockup">
    <div class="lockup__rule"></div>
    <div class="lockup__body">
      <div class="lockup__square"></div>
      <p class="lockup__name">Quorvell<br>Interior Designs</p>
    </div>
    <div class="lockup__rule"></div>
  </div>
</section>

</body>
</html>
```